Velmar Cyber Security (Consultants)

We need a webdesign for a new website www.velmarcybersecurity.example.

A draft version of the website is online. You can also look at our linkedIn company page: http://www.linkedin.example/company/7412096

This is what we do:
We defend our cybersociety against the growing number of cyber threats in order to allow our society to prosper and evolve more safely into the digital age. We seek to protect 4 key pillars of our society: critical (industrial) infrastructures, medical systems, our intellectual property, and financial systems.

Velmar is specialised in IT & information security consultancy and positions itself as an independent partner. Our employees possess a unique mix of technical hands-on engineering and consulting skills. We invest time and resources to learn about existing open-source and commercial technologies in order to give better advice.

We are no-nonsense, practical and to the point.

We advise and guide organisations with the strategy, definition and technical implementation of security projects. We take ownership in aligning the existing business, operational and technical context.

Some requirements:
- Ideally you deliver a fully coded and designed static website. I am hosting the website on www.hostbay.example; you can use the technologies that are supported there.
- My existing company colors and logos need to be preserved (see existing websites & linkedIn page)
- I would like a white background (is the best fit for my existing logo's, and easiest to maintain afterwards)
Some examples, but please feel free: http://www.stoneward.example/ http://www.quevix.example/ )
- I will use twitter as a way to update my website with relevant news ; So I want the twitterfeed integrated in the website, certianly on the homepage; if possible on all pages. (www.twitter.example/velmarsecurity)
- I am using my linkedIn company page; I want at least the "Follow" company button to be integrated in the website. (http://www.linkedin.example/company/velmar-cybersecurity-consultants/)
- it should be possible for me to do some minor updates to the site.
- I need several nice banners that I could also re-use at my linkedIn webpage (linkedIn requires 646 x 220 pixels or larger banners)

- As I see it now, the website should have a Home page that immediately displays the core services we offer. A basic Jobs page. an about and contact page where people can leave their details behind.
- Optional: An industries tab where there are sub-sites possible
Updates

This project has just been garantueed! First and second place get a nice payment. Please send you designs. 

I need
- A ready to deploy basic HTML webpage
- 4 pages: Home, Services, Careers, About/contact
- Some nice banners designed on my mission statement (in the brief)

Thanks

Reason: We would like to receive some more designs from other designers.

Target Market(s)

From medium sized KMO's, to mainly big enterprises.
My focusses is on strategic consulting, So managers, decision takers & business people
The site should also attrack consultants that have technical skills and managerial skills...

Industry/Entity Type

Financial

Requirements
Must have
• - My existing company colors and logos need to be preserved (see existing websites & linkedIn page)
- I would like a clean, professional site, with a white background
- As I see it now, the website should have a Home page that immediately displays the core services we offer. A basic careers page. an about and contact page where people can leave their details behind.
Nice to have
• - it should be possible for me to do some minor updates to the site.

```html
<!DOCTYPE html>
<html lang="en">
<head>
<meta charset="utf-8">
<title>Velmar Cyber Security (Consultants)</title>
<link href="https://fonts.googleapis.com/css2?family=Oswald:wght@400;500;600&family=Open+Sans:wght@400;600;700&display=swap" rel="stylesheet">
<style>
:root{
  --red:#c3161c;
  --red-dark:#9e1015;
  --ink:#2a2a2a;
  --text:#6b6b6b;
  --muted:#9a9a9a;
  --line:#e3e3e3;
  --band:#f1f1f1;
  --hero-a:#1c1c1c;
  --hero-b:#3a3a3a;
  --footer:#2a2a2a;
  --footer-low:#1f1f1f;
  --white:#ffffff;
}
*{box-sizing:border-box;margin:0;padding:0}
html,body{width:807px;height:1200px;overflow:hidden;background:var(--white)}
body{font-family:'Open Sans',Arial,sans-serif;color:var(--text);font-size:9px;line-height:1.5}
.page{width:807px;height:1200px;position:relative}

/* header */
.site-header{height:60px;display:flex;align-items:center;justify-content:space-between;padding:0 40px 0 48px}
.brand{display:flex;align-items:center;gap:7px;font-family:'Open Sans',sans-serif;font-weight:700;font-size:24px;color:var(--red);letter-spacing:-.5px}
.brand-dot{width:16px;height:16px;border-radius:50%;background:var(--red)}
.main-nav{display:flex;gap:16px;font-size:9.5px;color:var(--ink)}
.main-nav .active{color:var(--red)}

/* hero */
.hero{height:305px;position:relative;background:linear-gradient(90deg,var(--hero-a) 0%,#2a2a2a 45%,var(--hero-b) 100%);overflow:hidden}
.hero-visual{position:absolute;right:90px;top:22px;width:330px;height:265px;border-radius:14px;background:linear-gradient(160deg,#6a6a6a 0%,#d8d8d8 45%,#8a8a8a 100%)}
.hero-copy{position:absolute;left:48px;top:65px;width:250px;color:var(--white)}
.hero-copy h1{font-family:'Oswald',sans-serif;font-weight:500;font-size:21px;line-height:1.25;letter-spacing:.3px;margin-bottom:12px}
.hero-copy p{font-size:8.5px;line-height:1.55;color:#e6e6e6;margin-bottom:18px}
.btn-red{display:inline-block;background:var(--red);color:var(--white);font-family:'Oswald',sans-serif;font-size:10px;letter-spacing:.5px;padding:7px 14px}
.slider-dots{display:flex;justify-content:center;gap:5px;margin-top:8px}
.slider-dots span{width:7px;height:7px;border-radius:50%;background:#cfcfcf}
.slider-dots span.on{background:var(--red)}

/* services */
.intro{text-align:center;margin-top:22px}
.intro h2{font-family:'Oswald',sans-serif;font-weight:600;font-size:23px;color:var(--ink);letter-spacing:.3px}
.intro h2 em{font-style:normal;color:var(--red)}
.intro p{font-family:'Oswald',sans-serif;font-size:11px;color:var(--ink);letter-spacing:.6px;margin-top:2px}
.services{display:flex;justify-content:center;gap:58px;margin-top:34px}
.service{width:180px;text-align:center}
.service-icon{width:52px;height:52px;border-radius:50%;background:var(--ink);margin:0 auto 14px;display:flex;align-items:center;justify-content:center}
.service h3{font-family:'Oswald',sans-serif;font-weight:500;font-size:14px;color:var(--red);line-height:1.1}
.service .tag{font-size:6.5px;font-weight:700;color:var(--ink);letter-spacing:.3px;margin:2px 0 9px}
.service p{font-size:7.5px;color:var(--muted);line-height:1.6}
.more{display:inline-block;margin-top:12px;border:1px solid var(--line);border-radius:3px;padding:3px 9px;font-size:7px;color:var(--muted)}
.more b{color:var(--red);font-weight:600}
.divider{width:715px;height:1px;background:var(--line);margin:26px auto 0}

/* about + blog */
.split{display:flex;justify-content:space-between;padding:26px 46px 0 58px}
.about{width:330px}
.about h3{font-family:'Oswald',sans-serif;font-weight:500;font-size:13px;color:var(--ink);margin-bottom:8px}
.about h3 em{font-style:normal;color:var(--red)}
.about p{font-size:7.5px;color:var(--muted);margin-bottom:7px}
.blog{width:300px;border:1px solid var(--line);padding:10px 12px}
.blog h4{font-family:'Oswald',sans-serif;font-weight:400;font-size:10px;color:var(--ink);margin-bottom:8px;display:flex;align-items:center;gap:5px}
.blog h4::before{content:"";width:5px;height:5px;background:var(--red)}
.post{display:flex;gap:8px;margin-bottom:8px}
.post-thumb{width:40px;height:34px;flex:none;background:linear-gradient(135deg,#bdbdbd,#e2e2e2)}
.post strong{display:block;font-size:7.5px;color:var(--ink)}
.post small{display:block;font-size:6.5px;color:var(--red)}
.post p{font-size:6.5px;color:var(--muted);line-height:1.45}

/* feed band */
.feed{position:absolute;left:0;top:985px;width:807px;height:52px;background:var(--band);display:flex;align-items:center;padding-left:58px;gap:14px}
.feed-mark{width:24px;height:24px;border-radius:50%;background:#3fa9e6}
.feed strong{display:block;font-family:'Oswald',sans-serif;font-weight:400;font-size:9px;color:var(--ink);letter-spacing:.4px}
.feed span{font-size:7px;color:var(--muted)}
.feed span b{color:var(--red);font-weight:600}

/* footer */
.site-footer{position:absolute;left:0;top:1037px;width:807px;height:163px;background:var(--footer);color:#bdbdbd}
.footer-cols{display:flex;padding:18px 0 0 58px;gap:0}
.footer-col{width:125px}
.footer-col h5{font-family:'Oswald',sans-serif;font-weight:400;font-size:10px;color:var(--white);margin-bottom:6px}
.footer-col li{list-style:none;font-size:7px;line-height:1.75;color:#a8a8a8}
.newsletter{width:250px;margin-left:40px}
.newsletter h5{font-family:'Oswald',sans-serif;font-weight:400;font-size:10px;color:var(--white);margin-bottom:6px}
.newsletter p{font-size:7px;color:#a8a8a8;margin-bottom:8px}
.subscribe{display:flex;height:18px}
.subscribe span{flex:1;background:var(--white);font-size:7px;color:var(--muted);padding:3px 6px}
.subscribe b{width:22px;background:var(--red);color:var(--white);font-size:7px;display:flex;align-items:center;justify-content:center}
.footer-base{position:absolute;bottom:0;left:0;width:100%;height:20px;background:var(--footer-low);font-size:6.5px;color:#8a8a8a;padding:5px 58px}
</style>
</head>
<body>
<div class="page">

  <header class="site-header">
    <div class="brand"><span class="brand-dot"></span>Velmar</div>
    <nav class="main-nav">
      <span>Home</span><span class="active">About Us</span><span>Our Services</span><span>Our Technology</span><span>Blog</span><span>Contact Us</span>
    </nav>
  </header>

  <section class="hero">
    <div class="hero-visual" role="img" aria-label="Hands holding a tablet showing a security dashboard"></div>
    <div class="hero-copy">
      <h1>CYBERSECURITY STRATEGY<br>ASSESSMENT &amp; ROADMAP</h1>
      <p>In this management consulting solution we assist and guide the Security Officer or the general management, in defining and implementing an effective cybersecurity strategy. The traditional compliance based security is failing.</p>
      <span class="btn-red">BECOME A CLIENT</span>
    </div>
  </section>

  <div class="slider-dots"><span></span><span></span><span class="on"></span><span></span></div>

  <section class="intro">
    <h2>DEFENDERS OF OUR CYBERSOCIETY. <em>SEE OUR ADVANTAGES</em></h2>
    <p>CHECK OUT OUR TOP CONSULTING SOLUTIONS &amp; SERVICES</p>
  </section>

  <section class="services">
    <article class="service">
      <div class="service-icon">
        <svg width="22" height="24" viewBox="0 0 22 24"><path d="M11 1 L20 4 V11 C20 17 15 21 11 23 C7 21 2 17 2 11 V4 Z" fill="none" stroke="#fff" stroke-width="2"/><path d="M7 12 L10 15 L15 9" fill="none" stroke="#fff" stroke-width="2"/></svg>
      </div>
      <h3>CYBERSECURITY STRATEGY</h3>
      <div class="tag">LEARN WHAT TO PROTECT</div>
      <p>We map your critical assets and threats, then shape a clear roadmap that aligns security choices with your business goals and daily operations.</p>
      <span class="more">Click here to <b>Read Reading</b> »</span>
    </article>
    <article class="service">
      <div class="service-icon">
        <svg width="24" height="24" viewBox="0 0 24 24"><circle cx="12" cy="12" r="4" fill="none" stroke="#fff" stroke-width="2"/><path d="M12 2v4M12 18v4M2 12h4M18 12h4M5 5l3 3M16 16l3 3M5 19l3-3M16 8l3-3" stroke="#fff" stroke-width="2"/></svg>
      </div>
      <h3>TOP-4 CYBER CONTROLS</h3>
      <div class="tag">TOP INTERNATIONAL CYBERSECURITY EXPERTS</div>
      <p>We put the four controls in place that block most attacks, tuned to your systems, so your teams gain protection quickly and with little friction.</p>
      <span class="more">Click here to <b>Read Reading</b> »</span>
    </article>
    <article class="service">
      <div class="service-icon">
        <svg width="22" height="24" viewBox="0 0 22 24"><rect x="3" y="10" width="16" height="12" rx="2" fill="none" stroke="#fff" stroke-width="2"/><path d="M7 10V6a4 4 0 0 1 8 0v4" fill="none" stroke="#fff" stroke-width="2"/></svg>
      </div>
      <h3>FREE IMPLEMENTATION</h3>
      <div class="tag">PEC IF SIGNED WITH OUR SERVICES</div>
      <p>Sign on for our consulting services and we handle the first rollout for free, working hands-on beside your engineers from plan to finish.</p>
      <span class="more">Click here to <b>Read Reading</b> »</span>
    </article>
  </section>

  <div class="divider"></div>

  <section class="split">
    <div class="about">
      <h3>A Little Bit <em>About Us...</em></h3>
      <p>The Velmar Consulting Team is an independent partner with measurable results. Our people mix hands-on engineering with consulting skills, and we invest in learning open-source and commercial tools to give better advice.</p>
      <p>We are no-nonsense, practical and to the point. We guide strategy, definition and technical delivery of your security projects.</p>
      <span class="more">Click here to <b>Read Reading</b> »</span>
    </div>
    <aside class="blog">
      <h4>Latest Blog Posts</h4>
      <div class="post">
        <div class="post-thumb" role="img" aria-label="Blog post thumbnail"></div>
        <div>
          <strong>How We Map ICS Networks Without Downtime</strong>
          <small>Posted by Velmar Team · 12 comments</small>
          <p>A short look at safe discovery in industrial plants and what we learned along the way.</p>
        </div>
      </div>
      <div class="post">
        <div class="post-thumb" role="img" aria-label="Blog post thumbnail"></div>
        <div>
          <strong>Why Compliance Alone Keeps Failing</strong>
          <small>Posted by Velmar Team · 8 comments</small>
          <p>Checklists are not a strategy. Here is how to move to risk-based security planning.</p>
        </div>
      </div>
    </aside>
  </section>

  <section class="feed">
    <span class="feed-mark"></span>
    <div>
      <strong>LATEST POSTS FROM CHIRPLINE</strong>
      <span>@velmarsecurity · New report on critical infrastructure threats is now live · <b>about 2 hours ago</b></span>
    </div>
  </section>

  <footer class="site-footer">
    <div class="footer-cols">
      <div class="footer-col"><h5>Quick Links</h5><ul><li>Home</li><li>Cyber Security</li><li>Privacy Policy</li><li>Blog</li><li>Contact Us</li></ul></div>
      <div class="footer-col"><h5>About Us</h5><ul><li>Our Team</li><li>Careers</li><li>Industries</li><li>Partners</li><li>Press</li></ul></div>
      <div class="footer-col"><h5>Community</h5><ul><li>Events</li><li>Webinars</li><li>Newsletter</li><li>Resources</li><li>Support</li></ul></div>
      <div class="newsletter">
        <h5>Subscribe to our Newsletter</h5>
        <p>Get security insights and company news straight to your inbox.</p>
        <div class="subscribe"><span>Email address</span><b>OK</b></div>
      </div>
    </div>
    <div class="footer-base">© Velmar Cyber Security (Consultants) · www.velmarcybersecurity.example</div>
  </footer>

</div>
</body>
</html>
```